Visitenkarten-Design für Hotel und Restaurant in der Fußgängerzone
Zielgruppe
Hotel und Restaurant in der Fußgängerzone, zwei Gehminuten zum Bodensee.
Neu renoviertes Hotel/Restaurant (z.B.Boxspringbett, Holzboden, USB Steckdosen).
Übernachtung mit Frühstück im Einzel,-Doppel,- oder Komfortzimmer (für 3 Personen).
Restaurant mit regionaler Küche. Besondere saisonale Zutaten unserer Nachbarländer als Specials.
Touristen im Sommer Durchschnittalter: 50 Jahre, sportlich, modern, gut betucht.
Einwohner der Stadt im Winter, Alter zwischen 25 und 65 Jahre, viele davon Hausbesitzer, Segelboot Besitzer etc.
Aufgabenstellung
Farbkonzept im Restaurant:
warm- weiße Wände, dunkle Holzmöbel, rote Barelemente, weiß-kupferfarbene Lampen.
Würden uns etwas minimalistisches wünschen, trotzdem mit einem Wow Effekt.
Sei es ein ausgeschnittenes Logo, abgerundete Ecken, besonderes Material usw.
Dateianhänge sind nur für´s bessere Verständnis, muss nicht zwingend als Vorgabe gesehen werden.
Vorderseite:
Logo
Hotel & Restaurant (kann, muss aber nicht draufstehen.)
zum Anker
Seeufer

```html
<!DOCTYPE html>
<html lang="de">
<head>
<meta charset="utf-8">
<title>zum Anker – Visitenkarte</title>
<link rel="stylesheet" href="https://fonts.googleapis.com/css2?family=Fira+Sans+Condensed:wght@300;400;600&family=Josefin+Sans:wght@300&display=swap">
<style>
  :root {
    --paper: #ffffff;
    --card: #000000;
    --ink: #ffffff;
    --accent: #fde60f;
    --curl: #2a2728;
  }
  * { margin: 0; padding: 0; box-sizing: border-box; }
  html, body { width: 1200px; height: 1005px; overflow: hidden; background: var(--paper); }
  .sheet { position: relative; width: 1200px; height: 1005px; }
  .card {
    position: absolute; top: 87px; height: 840px; background: var(--card);
    color: var(--ink); font-family: "Fira Sans Condensed", sans-serif; overflow: hidden;
  }
  .card--front { left: 66px; width: 513px; }
  .card--back { left: 606px; width: 517px; }
  .brand { position: absolute; left: 0; width: 100%; text-align: center; }
  .brand__mark {
    display: block; margin: 0 auto; border-radius: 50%;
    border: 14px solid var(--ink);
  }
  .brand__name {
    display: block; font-weight: 600; line-height: 1; letter-spacing: 1px;
    white-space: nowrap;
  }
  .brand__place {
    display: flex; align-items: center; justify-content: center; gap: 20px;
    font-family: "Josefin Sans", sans-serif; font-weight: 300; letter-spacing: 5px;
    color: var(--ink);
  }
  .brand__place::before, .brand__place::after {
    content: ""; height: 2px; background: var(--ink); width: 66px;
  }
  .card--front .brand { top: 245px; }
  .card--front .brand__mark { width: 154px; height: 154px; }
  .card--front .brand__name { font-size: 76px; margin-top: 22px; }
  .card--front .brand__place { font-size: 28px; margin-top: 18px; }
  .card--back .brand { top: 118px; }
  .card--back .brand__mark { width: 142px; height: 142px; }
  .card--back .brand__name { font-size: 70px; margin-top: 22px; }
  .card--back .brand__place { font-size: 25px; margin-top: 14px; }
  .web {
    position: absolute; left: 0; width: 100%; top: 778px;
    text-align: center; font-size: 23px; letter-spacing: 0.3px;
  }
  .contact { position: absolute; left: 30px; top: 637px; }
  .contact__mail { font-size: 24px; }
  .contact__address { font-size: 28px; margin-top: 6px; }
  .contact__address .city, .contact__phone { color: var(--accent); }
  .contact__label { font-size: 25px; font-weight: 300; margin-top: 4px; }
  .contact__phone { font-size: 76px; line-height: 1; margin-top: -2px; letter-spacing: -0.5px; }
  .corner { position: absolute; left: 0; top: 0; }
</style>
</head>
<body>
<div class="sheet">
  <section class="card card--front">
    <div class="brand">
      <span class="brand__mark"></span>
      <span class="brand__name">zum Anker</span>
      <div class="brand__place">Seeufer</div>
    </div>
    <p class="web">www.zum-anker-seeufer.de</p>
  </section>

  <section class="card card--back">
    <svg class="corner" width="95" height="90" viewBox="0 0 95 90" aria-hidden="true">
      <path d="M0 0 H89 C70 8 60 25 55 40 C40 52 20 60 0 87 Z" fill="var(--accent)"/>
      <path d="M89 0 C70 8 60 25 55 40 C40 52 20 60 0 87 L0 90 L95 0 Z" fill="var(--card)"/>
      <path d="M55 40 C40 52 25 62 15 75 C35 68 52 66 66 67 C60 58 57 50 55 40 Z" fill="var(--curl)"/>
    </svg>
    <div class="brand">
      <span class="brand__mark"></span>
      <span class="brand__name">zum Anker</span>
      <div class="brand__place">Seeufer</div>
    </div>
    <div class="contact">
      <p class="contact__mail">info@zum-anker-seeufer.de</p>
      <p class="contact__address">Lindengasse 12, <span class="city">00000 Musterhafen</span></p>
      <p class="contact__label">phone:</p>
      <p class="contact__phone">00 123 456 789</p>
    </div>
  </section>
</div>
</body>
</html>
```